Marketing Expert Needs a Book Cover Design to Inspire Audiences

Need a book cover design for my first book!
The book is a ‘How To’ serious non fiction book. It has insights for marketers on how to transform their marketing to help their organizations accelerate sales and drive growth. This is not a high level theoretical book about brand building. Instead this includes strategic frameworks, and tried and tested ideas and tactics which marketers (or aspiring marketers) can use to be successful in their jobs. The premise of this book is that it’s no longer enough for marketers to focus on brand recognition. We need to help the business to create demand and make it easier for our sales colleagues to close deals.
The aim is to inspire readers with insights so that they think differently about themselves and their marketing. The aim is to compel them to take start new conversations to accelerate sales, using the tools, concepts and case studies outlined in the book.
The Title: The Growth Signal
Subtitle: Steps to Win Buyers by Storytelling, Curiosity and Trusted Voices.
The cover must have a compelling visual which communicates this idea-
The Growth Signal Inspires You to Think Different so That You Scale/Overcome the Limits you might have placed on yourself or your business.
I like a simple and clean look. I'm attaching some samples which I like. Looking to achieve the same look for my book cover.
Update- I need the cover for an ebook only. Since the cover will be displayed as a thumbnail in Verbolt and other online shopping sites, it should be without any clutter with good contrast between images and text. This will help with visibility.
Updates
Key Art Style designs will also be welcome. Added Saturday, September 24, 2016
Reason: I'm hoping that atleast some more top 20 designers will respond.
Target Market(s)
Target market is CMOs, Marketing Managers, Business Leaders, MBA students- anyone who is looking to reshape and rejig their marketing skills and teams.
Industry/Entity Type
Marketing
Requirements
Must have
- A compelling visual is a must have.
- It shouldn't have only text.
Nice to have
- Please refer the cover samples I sent.
- Key Art designs will also be welcome.
Should not have
- Clutter.
- I like simplicity.

```html
<!DOCTYPE html>
<html lang="en">
<head>
<meta charset="utf-8">
<title>The Growth Signal — Ebook Cover</title>
<link rel="stylesheet" href="https://fonts.googleapis.com/css2?family=Bebas+Neue&family=Tinos:wght@700&display=swap">
<style>
  :root {
    --page-bg: #ffffff;
    --cover-blue: #0854a1;
    --title-yellow: #f9e921;
    --figure-teal: #2aa7c4;
    --figure-skin: #f3d9a9;
    --figure-glass: #bfe3e4;
  }
  html, body {
    margin: 0;
    padding: 0;
    width: 1200px;
    height: 1000px;
    overflow: hidden;
    background: var(--page-bg);
  }
  .canvas {
    position: relative;
    width: 1200px;
    height: 1000px;
  }
  .cover {
    position: absolute;
    left: 265px;
    top: 62px;
    width: 615px;
    height: 878px;
    background: var(--cover-blue);
    overflow: hidden;
  }
  .cover-visual {
    position: absolute;
    left: 240px;
    top: 412px;
    width: 360px;
    height: 436px;
    z-index: 1;
  }
  .cover-title {
    position: absolute;
    left: 0;
    top: 0;
    width: 615px;
    height: 410px;
    z-index: 2;
  }
  .cover-title text {
    font-family: "Bebas Neue", "Oswald", sans-serif;
    fill: var(--title-yellow);
  }
  .cover-subtitle {
    position: absolute;
    left: 35px;
    top: 416px;
    width: 200px;
    margin: 0;
    font-family: "Tinos", "Times New Roman", serif;
    font-weight: 700;
    font-size: 25px;
    line-height: 31.5px;
    color: var(--title-yellow);
    z-index: 2;
  }
  .cover-subtitle span { display: block; white-space: nowrap; }
</style>
</head>
<body>
<main class="canvas">
  <section class="cover">
    <svg class="cover-visual" viewBox="0 0 360 436" role="img"
         aria-label="Illustration of a businessman in a teal suit peering through a large magnifying glass at a glowing light bulb">
      <defs>
        <linearGradient id="visual-tone" x1="0" y1="0" x2="1" y2="1">
          <stop offset="0" stop-color="var(--figure-skin)"/>
          <stop offset="0.45" stop-color="var(--figure-glass)"/>
          <stop offset="1" stop-color="var(--figure-teal)"/>
        </linearGradient>
      </defs>
      <rect x="0" y="0" width="360" height="436" rx="24" fill="url(#visual-tone)"/>
    </svg>

    <svg class="cover-title" viewBox="0 0 615 410" aria-labelledby="book-title">
      <title id="book-title">The Growth Signal</title>
      <text x="35" y="108" font-size="106" textLength="120" lengthAdjust="spacingAndGlyphs">THE</text>
      <text x="33" y="308" font-size="258" textLength="362" lengthAdjust="spacingAndGlyphs">GROWTH</text>
      <text x="35" y="403" font-size="106" textLength="360" lengthAdjust="spacingAndGlyphs">SIGNAL</text>
    </svg>

    <p class="cover-subtitle">
      <span>Steps to</span>
      <span>Win Buyers</span>
      <span>by</span>
      <span>Storytelling,</span>
      <span>Curiosity</span>
      <span>and Trusted</span>
      <span>Voices.</span>
    </p>
  </section>
</main>
</body>
</html>
```